Existing Plorv Website Redesign

Our current website is in need of redesign for the plorv.com platform. https://www.kestrawanders.com.au/ <br/>In addition to the brief below, we need the Website to be Multi – Lingual : English, Japanese, German, Dutch, French, Italian, Chinese Mandarin and Chinese Cantonese & Korean<br/><br/>All the content is already listed on the website. The successful design will implement the website with the current content and edit this including correct headers and URL addresses.<br/><br/>Company Profile-<br/>Kestra Wanders enhances the travellers' life experience through the wonder, discovery, adventure and cultural immersion of high quality tours throughout Papua New Guinea.<br/><br/>Our mission is to design and conduct safe, educational and exciting tours which:<br/><br/>cater for a range of ages, interests and budgets; respect local communities; promote sustainable tourism, leaving with them special memories.<br/><br/> <br/><br/>The current target demographic for Kestra Wanders of Papua New Guinea is the 50+ age group, primarily in Australia and New Zealand, but also the United States, Japan, Europe (Germany, France Italy & Britain and also China as it’s outbound visitor market matures and seeks new adventures.<br/><br/>We offer fully escorted small group tours and holidays that are safe, fully organised and guided for all age groups, nationalities and budgets.<br/><br/>PNG is uniquely placed as an attractive destination, showcasing the oldest, authentic surviving culture on earth! <br/><br/>Over 800 tribes generously share their customs, art, music, carvings, costumes and dances at a range of Festivals or “sing sings” held across the highlands and islands of this most picturesque of countries providing visiting culture enthusiasts and photographers with lasting memories and vivid images. Traversing the Pacific’s “Rim of Fire”, visitors are presented with a daily feast of scenery with the best nature has to offer amongst it’s big mountainous jungles and forests, untamed rivers, volcanic landscapes and pristine marine environments. Photograph animals, plants and exotic birds including the globally renowned Birds of Paradise.<br/><br/>The key group to target amongst the over 50’s are the Baby Boomers who are those born between 1946 to 1964.<br/><br/> <br/><br/>Baby boomers are also seeking an authentic experience whilst travelling. They want to go where the locals go, immersing themselves fully to experience and learn about a new culture.<br/><br/>According to the Global Voyaging Council, boomers are more likely to seek out educational and cultural experiences. What boomers really want is to be intellectually stimulated, which is why an experienced, knowledgeable and well-trained guide, such as Mark Delriss and those guides that he trains are necessary to attract them to these tours. Mark has immersed himself in the many periods of colonial occupier history along with a sound understanding of the first peoples and their cultures and Melanesian lifestyles.<br/><br/>As a destination Papua New Guinea will attract the baby boomers that are “young at heart” who actively seek out adventure, sometimes as a form of self-discovery. Knowing that they want to experience new adventures while being safe, Kestra Wanders has created adventure in a semi-controlled environment for the baby boomer.<br/><br/>Kestra Wanders of Papua New Guinea will be of interest primarily to the “Baby Boomer” demographic in Australia, many who have a fond familiarity with their neighbouring ex-colony. Their parents may have been involved in PNG in the pre-independence era as First and Second World War military personal, “Kiap” patrol officers, nurses, teachers,missionaries, tradesmen or public servants.<br/><br/>Potential visitors will discover a little known destination where the traditional Melanesian culture with over 800 tribes and languages, thrive and where, outside the major regional centres, little has changed in thousands of years.

Target Market(s)

Travel and Tourism

Colors

Designer to choose colors to be used in the design.

Requirements
Must have
• Website to be Multi – Lingual : English, Japanese, German, Dutch, French, Italian, Chinese Mandarin and Chinese Cantonese & Korean
• The successful design will implement the website with the current content and edit this including correct headers and URL addresses.

```html
<!DOCTYPE html>
<html lang="en">
<head>
<meta charset="utf-8">
<title>Kestra Wanders of Papua New Guinea</title>
<link rel="stylesheet" href="https://fonts.googleapis.com/css2?family=Oswald:wght@300;400&family=Josefin+Sans:wght@300;400&display=swap">
<style>
:root{
  --ink:#1c1c1c;
  --dark:#222222;
  --nav-text:#e6e6e6;
  --nav-muted:#9a9a9a;
  --band:#ececec;
  --soft:#f4f4f4;
  --line:#c9c9c9;
  --text:#333333;
  --white:#ffffff;
  --map:#d6dcdd;
}
*{margin:0;padding:0;box-sizing:border-box}
html,body{width:1200px;height:4971px;overflow:hidden;background:var(--white)}
body{font-family:'Josefin Sans',sans-serif;font-weight:300;color:var(--text);position:relative}
section,header,footer{position:absolute;left:0;width:1200px}
.heading{font-family:'Oswald',sans-serif;font-weight:300;color:var(--ink);text-transform:uppercase;text-align:center;letter-spacing:.5px}

.topnav{top:0;height:64px;background:var(--dark)}
.topnav a{position:absolute;top:24px;font-size:14px;font-weight:400;letter-spacing:1.2px;color:var(--nav-text);text-decoration:none;text-transform:uppercase}
.topnav a.active{color:var(--nav-muted)}

.brandbar{top:64px;height:151px;background:var(--white)}
.brand{position:absolute;left:0;width:1200px;top:30px;text-align:center}
.brand-name{font-family:'Oswald',sans-serif;font-weight:400;font-size:46px;color:var(--ink);text-transform:uppercase;line-height:1;display:inline-flex;align-items:center;gap:14px}
.brand-name .mark{width:14px;height:14px;border-radius:50%;background:var(--ink)}
.brand-sub{font-family:'Oswald',sans-serif;font-weight:400;font-size:20px;color:var(--ink);margin-top:6px}

.hero{top:215px;height:566px;background:linear-gradient(180deg,#2a8fd0 0%,#1a74b4 30%,#cf7f2c 48%,#d99a3a 58%,#16608f 75%,#0c3f63 100%)}

.booking{top:781px;height:174px;background:var(--band)}
.booking label{position:absolute;top:56px;font-size:12px;color:#555}
.field{position:absolute;top:77px;height:41px;border:1px solid var(--line);background:var(--white);font-size:13px;color:#aaa;padding:13px 12px;letter-spacing:.5px}
.field svg{position:absolute;right:10px;top:13px}
.btn{background:var(--ink);color:var(--white);text-align:center;font-size:16px;font-weight:300}
.search-btn{position:absolute;left:875px;top:77px;width:165px;height:41px;line-height:44px}

.welcome{top:955px;height:433px}
.welcome h1{position:absolute;top:82px;width:1200px;font-size:35px}
.welcome p{position:absolute;left:160px;width:880px;text-align:center;font-family:'Oswald',sans-serif;font-weight:300;font-style:italic;font-size:14px;line-height:29px;color:var(--text)}

.feature{top:1388px;height:557px;background:linear-gradient(100deg,#6b5a44 0%,#8a6a3e 18%,#c98a3c 28%,#4f5b35 45%,#3e4a2c 70%,#55603e 85%,#2f3624 100%)}
.card{position:absolute;left:412px;width:376px;background:rgba(255,255,255,.94);text-align:center}
.card h2{font-family:'Oswald',sans-serif;font-weight:300;font-size:27px;line-height:40px;color:var(--ink);text-transform:uppercase}
.card p{font-size:17px;line-height:32px;color:var(--text)}

.services{top:1945px;height:420px}
.services h2{position:absolute;top:85px;width:1200px;font-size:35px}
.service{position:absolute;top:165px;width:300px;text-align:center}
.service svg{display:block;margin:0 auto}
.service h3{font-family:'Oswald',sans-serif;font-weight:300;font-size:21px;color:var(--ink);text-transform:uppercase;margin-top:30px}
.service p{font-size:15.5px;line-height:27px;margin-top:6px}

.gallery{top:2365px;height:598px}
.gallery h2{position:absolute;top:14px;width:1200px;font-size:35px}
.photo{position:absolute;top:87px;width:287px;height:421px}

.review{top:2963px;height:560px;background:linear-gradient(90deg,#8a9a86 0%,#b07a5a 18%,#6b6a48 32%,#c7c0b0 50%,#6e8a96 66%,#a8645a 80%,#2f4652 100%)}

.contact{top:3523px;height:590px;background:var(--soft)}
.contact h2{position:absolute;top:86px;width:1200px;font-size:35px}
.contact-info{position:absolute;top:152px;width:1200px;text-align:center;font-family:'Oswald',sans-serif;font-weight:300;font-style:italic;font-size:15px;color:#777;text-transform:uppercase}
.contact-info .sep{margin:0 34px}
.input{position:absolute;background:var(--white);border:1px solid #e8e8e8;font-size:13px;color:#999;padding:12px 11px}
.send{position:absolute;left:286px;top:459px;width:629px;height:38px;line-height:41px}

.explore{top:4113px;height:725px}
.explore h2{position:absolute;top:86px;width:1200px;font-size:35px}
.worldmap{position:absolute;left:200px;top:157px;width:775px;height:380px;background:var(--map)}
.tagline{position:absolute;top:565px;width:1200px;text-align:center;font-size:25px;line-height:40px;color:#444;letter-spacing:.5px}

.sitefooter{top:4838px;height:133px;background:var(--dark)}
.social{position:absolute;top:53px;width:12px;height:12px;border-radius:50%;background:var(--white)}
.copyright{position:absolute;top:92px;width:1200px;text-align:center;font-size:12px;color:var(--nav-text)}
</style>
</head>
<body>

<header class="topnav">
  <a class="active" style="left:196px">Home</a>
  <a style="left:298px">Tours</a>
  <a style="left:409px">Birdwatching</a>
  <a style="left:583px">Gallery</a>
  <a style="left:708px">About Us</a>
  <a style="left:843px">Contact</a>
  <a style="left:972px">EN
    <svg width="10" height="8" viewBox="0 0 10 8"><path d="M1 2l4 4 4-4" stroke="#e6e6e6" stroke-width="1.6" fill="none"/></svg></a>
</header>

<section class="brandbar">
  <div class="brand">
    <div class="brand-name"><span class="mark"></span>Kestra Wanders</div>
    <div class="brand-sub">of Papua New Guinea</div>
  </div>
</section>

<section class="hero" role="img" aria-label="Diver beside an orange coral reef with a school of blue fish"></section>

<section class="booking">
  <label style="left:160px">Check In</label>
  <div class="field" style="left:160px;width:257px">DDMMYYYY
    <svg width="14" height="14" viewBox="0 0 14 14"><rect x="1.5" y="2.5" width="11" height="10" fill="none" stroke="#888"/><path d="M1.5 5.5h11M4 1v3M10 1v3" stroke="#888"/></svg></div>
  <label style="left:428px">Check Out</label>
  <div class="field" style="left:428px;width:257px">DDMMYYYY
    <svg width="14" height="14" viewBox="0 0 14 14"><rect x="1.5" y="2.5" width="11" height="10" fill="none" stroke="#888"/><path d="M1.5 5.5h11M4 1v3M10 1v3" stroke="#888"/></svg></div>
  <label style="left:698px">Adults</label>
  <div class="field" style="left:698px;width:75px">1
    <svg width="8" height="14" viewBox="0 0 8 14"><path d="M1 5l3-3 3 3M1 9l3 3 3-3" fill="#888"/></svg></div>
  <label style="left:786px">Kids</label>
  <div class="field" style="left:786px;width:75px">0
    <svg width="8" height="14" viewBox="0 0 8 14"><path d="M1 5l3-3 3 3M1 9l3 3 3-3" fill="#888"/></svg></div>
  <div class="btn search-btn">Search</div>
</section>

<section class="welcome">
  <h1 class="heading">Welcome to Kestra Wanders</h1>
  <p style="top:150px">Kestra Wanders is a tour operator specialising in Papua New Guinea and also Japan. All our destinations offer the ultimate experience for excitement, fun, adventure and cultural interaction. Come and discover the ancient lands and first peoples, experiencing up close the vividly spectacular and varied forms of customs, art, costumes and cuisine in the most culturally intact places in the world.</p>
  <p style="top:260px">Traversing the Pacific’s “Rim of Fire”, Kestra Wanders present you with a daily feast of scenery with the best nature has to offer amongst it’s big mountainous jungles and forests, untamed rivers, volcanic landscapes and pristine marine environments. Photograph the most exotic of birds, animals and plants in the most dramatic landscapes on earth. We offer fully escorted small group tours and holidays that are safe, fully organised and guided for all age groups, nationalities and budgets</p>
</section>

<section class="feature" role="img" aria-label="Close view of a traditional costume of leaves, feathers and woven fibre">
  <div class="card" style="top:94px;height:368px">
    <h2 style="margin-top:70px">Fully Escorted Small<br>Group Tours</h2>
    <p style="margin-top:10px">Safe Adventures of Papua<br>New Guinea</p>
    <div class="btn" style="margin:22px auto 0;width:165px;height:38px;line-height:41px">Get Started</div>
  </div>
</section>

<section class="services">
  <h2 class="heading">Our Services</h2>
  <div class="service" style="left:135px">
    <svg width="46" height="40" viewBox="0 0 46 40" fill="none" stroke="#444" stroke-width="1.4"><path d="M6 18h28v8a10 10 0 0 1-10 10h-8A10 10 0 0 1 6 26z"/><path d="M34 21h4a4 4 0 0 1 0 8h-5"/><path d="M15 6c-2 3 2 5 0 8M21 4c-2 3 2 5 0 8M27 6c-2 3 2 5 0 8"/></svg>
    <h3>Breakfast</h3>
    <p>Lorem ipsum dolor sit amet,<br>consectetur adipiscing elit, sed do<br>eiusmod tempor incididunt</p>
  </div>
  <div class="service" style="left:449px">
    <svg width="46" height="40" viewBox="0 0 46 40" fill="none" stroke="#444" stroke-width="1.6"><path d="M5 14a26 26 0 0 1 36 0M10 20a18 18 0 0 1 26 0M15 26a10 10 0 0 1 16 0"/><circle cx="23" cy="32" r="2" fill="#444"/></svg>
    <h3>Free WiFi</h3>
    <p>Lorem ipsum dolor sit amet,<br>consectetur adipiscing elit, sed do<br>eiusmod tempor incididunt</p>
  </div>
  <div class="service" style="left:762px">
    <svg width="46" height="40" viewBox="0 0 46 40" fill="none" stroke="#444" stroke-width="1.4"><circle cx="18" cy="12" r="8"/><path d="M18 20v14M8 34h30M24 26h14v8"/></svg>
    <h3>Garden</h3>
    <p>Lorem ipsum dolor sit amet,<br>consectetur adipiscing elit, sed do<br>eiusmod tempor incididunt</p>
  </div>
</section>

<section class="gallery">
  <h2 class="heading">Gallery</h2>
  <div class="photo" style="left:160px;background:linear-gradient(90deg,#5f9a34 0%,#b5182a 22%,#8e1020 42%,#4f8a2c 50%,#c21c2c 62%,#921424 80%,#7fae3e 100%)" role="img" aria-label="Two red lorikeets perched among green leaves"></div>
  <div class="photo" style="left:457px;background:linear-gradient(180deg,#7a6250 0%,#b3806a 25%,#c06a8a 50%,#587236 72%,#6b5a3a 100%)" role="img" aria-label="Highland dancers in festival costume"></div>
  <div class="photo" style="left:754px;background:linear-gradient(180deg,#aebfca 0%,#7e8a6a 22%,#5a4e3e 45%,#6a5a44 62%,#4f8a30 78%,#6cad3c 100%)" role="img" aria-label="Traditional spirit house with dancers on a lawn"></div>
</section>

<section class="review" role="img" aria-label="Travellers holding carved masks and shields by a river">
  <div class="card" style="top:97px;height:368px">
    <h2 style="margin-top:62px;font-size:26px">Guest Review</h2>
    <svg width="26" height="18" viewBox="0 0 26 18" style="margin-top:6px"><path d="M10 2C4 4 2 8 2 12a4 4 0 1 0 4-4M22 2c-6 2-8 6-8 10a4 4 0 1 0 4-4" fill="none" stroke="#333" stroke-width="1.6"/></svg>
    <p style="margin-top:6px">Lorem ipsum dolor sit amet,<br>consectetur adipiscing elit,<br>sed do eiusmod tempor incididunt</p>
    <svg width="64" height="8" viewBox="0 0 64 8" style="margin-top:28px"><circle cx="4" cy="4" r="3" fill="#222"/><circle cx="22" cy="4" r="3" fill="#bbb"/><circle cx="40" cy="4" r="3" fill="#bbb"/><circle cx="58" cy="4" r="3" fill="#bbb"/></svg>
  </div>
</section>

<section class="contact">
  <h2 class="heading">Contact Us</h2>
  <div class="contact-info">info@kestrawanders.com.au<span class="sep">/</span>+61 400 555 218<span class="sep">/</span>P.O. Box 4417 Ashgrove Vale 3160 Melbourne</div>
  <div class="input" style="left:285px;top:218px;width:307px;height:39px">Name</div>
  <div class="input" style="left:606px;top:218px;width:307px;height:39px">Email</div>
  <div class="input" style="left:285px;top:271px;width:628px;height:39px">Subject</div>
  <div class="input" style="left:285px;top:324px;width:628px;height:121px">Message</div>
  <div class="btn send">Send</div>
</section>

<section class="explore">
  <h2 class="heading">Explore the Unknown with Us</h2>
  <div class="worldmap" role="img" aria-label="World map highlighting Japan and Papua New Guinea in red"></div>
  <div class="tagline">Your PAPUA NEW GUINEA Expert<br>Bespoke Tours of Japan</div>
</section>

<footer class="sitefooter">
  <div class="social" style="left:573px" role="img" aria-label="Social link"></div>
  <div class="social" style="left:612px" role="img" aria-label="Social link"></div>
  <div class="copyright">Copyright 2019 © The Company Name &nbsp;All Rights Reserved</div>
</footer>

</body>
</html>
```